7 Loop Flyer

We are a gym named Korvalle and we need a flyer design for our challenge we will be having called the '7 LOOP'. The '7 LOOP' is a 6 Week Transformation Challenge where participants will train throughout the 6 weeks then see what progress they have made at the end, with prizes on offer for the best results.

We would like to see designs that use the colour blue.

The design we would like has been sketched and added in files section, subject to minor word changes later on. Both logos have also been added to the file section as well. As per the sketch, At the top should be the 'Korvalle 7 LOOP' logo. Underneath will have writing that says 'A 6 week transformation challenge that will get you in the best shape of your life!

Below that will say 'NO EGOS REAL PEOPLE REAL RESULTS' underneath each other. With 'ENTRIES NOW OPEN' below.

Then at the bottom the other Korvalle logo.

Colors
33a6d7
85cae6
0292cd
0355a3
3276b5
85abd2
e667a6
e34197

Requirements
Must have
• Mention of the prizes
• "Chance to win over $1200 in prizes"
• 1st Place $600 CASH MONEY!!!!
• Sign up now kicks off September 22
• The ultimate 6 Week Transformation
Should not have
• Generic / Stock images

```html
<!DOCTYPE html>
<html lang="en">
<head>
<meta charset="utf-8">
<title>Korvalle 7 LOOP Flyer</title>
<link rel="stylesheet" href="https://fonts.googleapis.com/css2?family=Oswald:wght@300;400;500;700&display=swap">
<style>
  :root {
    --paper: #f3f3f3;
    --ink: #2f2f30;
    --sky: #33a6d7;
    --ocean: #0292cd;
    --navy: #0355a3;
    --mid-blue: #3276b5;
    --pink: #e34197;
    --pink-soft: #e667a6;
    --badge: #4a4a4c;
    --badge-light: #5c5c5e;
    --white: #ffffff;
  }
  * { margin: 0; padding: 0; box-sizing: border-box; }
  html, body { width: 946px; height: 1200px; overflow: hidden; background: var(--paper); }
  .flyer {
    position: relative;
    width: 946px;
    height: 1200px;
    background: var(--paper);
    font-family: "Oswald", "Arial Narrow", sans-serif;
    color: var(--ink);
    overflow: hidden;
  }
  .photo {
    position: absolute;
    left: 457px; top: 30px;
    width: 489px; height: 900px;
    background: radial-gradient(ellipse at 50% 35%, #d9b08e 0%, #c9a07f 22%, #3a3a3c 48%, #2b2b2d 75%, var(--paper) 100%);
    opacity: .9;
  }
  .event-mark {
    position: absolute;
    left: 45px; top: 42px;
    width: 314px; height: 217px;
    display: flex; flex-direction: column; align-items: center; justify-content: center;
  }
  .event-mark .dot {
    width: 34px; height: 34px; border-radius: 50%;
    background: var(--ink); margin-bottom: 12px;
  }
  .event-mark .name {
    font-weight: 700; font-size: 46px; line-height: 1; letter-spacing: 1px;
    text-transform: uppercase; color: var(--ink);
  }
  .event-mark .tag {
    margin-top: 8px; font-weight: 700; font-size: 17px; letter-spacing: 1px;
    text-transform: uppercase; color: var(--ink);
  }
  .intro {
    position: absolute; left: 49px; top: 300px;
    font-weight: 300; font-size: 27px; line-height: 37px; letter-spacing: -0.5px;
  }
  .intro .big { display: block; font-weight: 400; font-size: 48px; line-height: 56px; margin-top: 2px; }
  .checklist { position: absolute; left: 49px; top: 450px; list-style: none; }
  .checklist li {
    display: flex; align-items: center; height: 54px;
    font-weight: 400; font-size: 42px; color: var(--ocean); text-transform: uppercase; letter-spacing: -0.5px;
  }
  .checklist svg { width: 38px; height: 34px; margin-right: 18px; }
  .prize-intro { position: absolute; left: 49px; top: 640px; color: var(--pink); font-weight: 400; }
  .prize-intro .lead { font-size: 35px; line-height: 44px; }
  .prize-intro .amount { font-size: 58px; line-height: 66px; text-transform: uppercase; letter-spacing: -1px; }
  .details {
    position: absolute; left: 53px; top: 780px;
    font-weight: 300; font-size: 22px; line-height: 33px; letter-spacing: -0.3px;
  }
  .wave { position: absolute; left: 0; top: 0; width: 946px; height: 1200px; }
  .badge { position: absolute; left: 568px; top: 677px; width: 270px; height: 270px; }
  .badge-text {
    position: absolute; left: 568px; top: 677px; width: 270px; height: 270px;
    display: flex; flex-direction: column; align-items: center; justify-content: center;
    color: var(--pink-soft); font-weight: 500; text-transform: uppercase;
  }
  .badge-text .place { font-size: 30px; line-height: 36px; text-transform: none; }
  .badge-text .cash { font-size: 58px; line-height: 62px; font-weight: 700; }
  .badge-text .note { font-size: 31px; line-height: 38px; }
  .entries {
    position: absolute; left: 49px; top: 1042px;
    color: var(--pink); font-weight: 400; font-size: 72px; line-height: 78px; text-transform: uppercase; letter-spacing: -1.5px;
  }
  .studio {
    position: absolute; left: 470px; top: 1010px; width: 420px; text-align: center; color: var(--white);
  }
  .studio .name { font-weight: 700; font-size: 86px; line-height: 94px; letter-spacing: 3px; text-transform: uppercase; }
  .studio .service { margin-top: 6px; font-weight: 500; font-size: 33px; line-height: 38px; letter-spacing: 1px; text-transform: uppercase; }
</style>
</head>
<body>
<main class="flyer">
  <div class="photo" role="img" aria-label="Photo of a smiling athlete in a black and pink sports top and leggings, hands on hips"></div>

  <header class="event-mark">
    <span class="dot"></span>
    <span class="name">Korvalle 7 LOOP</span>
    <span class="tag">Made in the Harbour</span>
  </header>

  <p class="intro">A 6 week transformation challenge<br>that will get you in the best shape<span class="big">OF YOUR LIFE!</span></p>

  <ul class="checklist">
    <li><svg viewBox="0 0 38 34"><rect x="2" y="6" width="26" height="24" rx="4" fill="none" stroke="var(--ocean)" stroke-width="3"/><path d="M8 17 L15 24 L35 3" fill="none" stroke="var(--ocean)" stroke-width="3.5" stroke-linecap="round" stroke-linejoin="round"/></svg>No egos</li>
    <li><svg viewBox="0 0 38 34"><rect x="2" y="6" width="26" height="24" rx="4" fill="none" stroke="var(--ocean)" stroke-width="3"/><path d="M8 17 L15 24 L35 3" fill="none" stroke="var(--ocean)" stroke-width="3.5" stroke-linecap="round" stroke-linejoin="round"/></svg>Real people</li>
    <li><svg viewBox="0 0 38 34"><rect x="2" y="6" width="26" height="24" rx="4" fill="none" stroke="var(--ocean)" stroke-width="3"/><path d="M8 17 L15 24 L35 3" fill="none" stroke="var(--ocean)" stroke-width="3.5" stroke-linecap="round" stroke-linejoin="round"/></svg>Real results</li>
  </ul>

  <div class="prize-intro">
    <p class="lead">Chance to win over</p>
    <p class="amount">$1200 in prizes</p>
  </div>

  <p class="details">Sign up now kicks off September 22<br>The ultimate 6 Week Transformation</p>

  <svg class="wave" viewBox="0 0 946 1200" aria-hidden="true">
    <defs>
      <linearGradient id="blueBand" x1="0" y1="0" x2="1" y2="0">
        <stop offset="0" stop-color="#00aeef"/>
        <stop offset=".5" stop-color="#0292cd"/>
        <stop offset="1" stop-color="#0355a3"/>
      </linearGradient>
    </defs>
    <path d="M0 905 C180 960 420 860 600 800 C720 760 840 745 946 750 L946 830 C760 835 560 900 380 960 C220 1010 90 1000 0 945 Z" fill="var(--pink-soft)"/>
    <path d="M0 925 C180 985 420 885 600 825 C720 785 840 770 946 775 L946 830 C760 835 560 900 380 960 C220 1010 90 1000 0 945 Z" fill="var(--pink)"/>
    <path d="M0 945 C90 1000 220 1010 380 960 C560 900 760 835 946 830 L946 1200 L0 1200 Z" fill="url(#blueBand)"/>
  </svg>

  <svg class="badge" viewBox="0 0 270 270" aria-hidden="true">
    <circle cx="135" cy="135" r="118" fill="var(--badge)" stroke="var(--badge)" stroke-width="18" stroke-dasharray="5 4"/>
    <circle cx="135" cy="135" r="112" fill="var(--badge)"/>
    <path d="M40 130 A95 95 0 0 1 230 130 Z" fill="var(--badge-light)"/>
  </svg>
  <div class="badge-text">
    <span class="place">1st Place</span>
    <span class="cash">$600</span>
    <span class="note">Cash money!!!!</span>
  </div>

  <p class="entries">Entries<br>now open</p>

  <footer class="studio">
    <p class="name">Korvalle</p>
    <p class="service">Personal &amp;<br>Group Training</p>
  </footer>
</main>
</body>
</html>
```